WP website design (Brenmoor)

We need a wordpress design for an established auction and real estate company based in Kentucky. The winning design will incorporate a professional color scheme with company logo in a clean layout with specified widgets. The design needs to consider that this will be developed on a responsive theme. Color is #307d84, with gray/black or other as an accent/highlight color.

Industry/Entity Type

Real Estate

Requirements
Must have
• Elelments of design need to consider that this site is going to be developed on a responsive theme.

Navigation:
1) Home 2) Current Auctions 3) Past Auctions 4) Meet the Staff 5) For Sellers 6) For Buyers 7) Testimonials 8) Contact Us

Colors will be the blue of logo plus black/gray or other accent color.

Slideshow will be prominent, please use stock real estate photo for initial image. Will have following in either header or sidebar: testimonials, social icons (FB, linkedin Twitter, RSS), Featured Auctions widget, newsletter signup form.

Footer will have contact info (below) and attached affiliation logos.
Brenmoor Auctions, Inc.
8415 Tamsen Rd., Louisville KY 40291
glen.office@brenmoorbid.example
Phone: (502) 736 2048

```html
<!DOCTYPE html>
<html lang="en">
<head>
<meta charset="utf-8">
<title>Brenmoor Auctions</title>
<link href="https://fonts.googleapis.com/css2?family=Raleway:wght@500;600;700;800&family=Roboto:ital,wght@0,400;0,500;1,400;1,500&display=swap" rel="stylesheet">
<style>
:root{
  --teal:#0e8284;
  --teal-dark:#0b6f71;
  --amber:#f5a623;
  --nav-active:#fbbf47;
  --grey-band:#e2e2e2;
  --footer:#555555;
  --ink:#222;
  --rule:#b9b9b9;
}
*{box-sizing:border-box;margin:0;padding:0}
html,body{width:960px;height:1200px;overflow:hidden;background:#fff}
body{position:relative;font-family:"Roboto",Arial,sans-serif;color:var(--ink)}
.abs{position:absolute}
.brand{font-family:"Raleway",Arial,sans-serif;font-weight:800;color:var(--teal);letter-spacing:1px}
.site-logo{left:80px;top:24px;font-size:38px;line-height:40px}
.site-logo small{display:block;font-size:22px;line-height:26px;letter-spacing:2px}
.signup{left:590px;top:17px;width:289px;height:69px;border:1px solid #d6d6d6;border-radius:3px;background:#fff}
.signup .field{position:absolute;left:12px;width:169px;height:20px;border:1px solid #e0e0e0;font-size:9px;color:#888;padding:4px 6px;font-family:"Raleway",sans-serif}
.signup .btn{position:absolute;left:196px;top:9px;width:79px;height:50px;background:var(--teal);color:#fff;border-radius:3px;font:700 16px/50px "Raleway",sans-serif;text-align:center;letter-spacing:.5px}
.nav{left:0;top:110px;width:960px;height:36px;background:var(--teal);display:flex;padding-left:78px}
.nav a{color:#fff;text-decoration:none;font:600 10.5px/36px "Raleway",sans-serif;padding:0 14px;border-right:1px solid rgba(255,255,255,.18)}
.nav a.active{background:var(--nav-active);color:#222;padding:0 8px;border:none}
.nav a:last-child{border:none}
.band{left:0;top:146px}
.hero{left:79px;top:159px;width:801px;height:357px;border:4px solid #000;background:linear-gradient(180deg,#6fa4d8 0%,#b9d3e8 35%,#d7cfc1 55%,#6d9a3f 80%,#4b7d2b 100%)}
.welcome{left:0;top:537px;width:960px;text-align:center;font:700 20px "Raleway",sans-serif;color:var(--teal);letter-spacing:.5px}
.intro{left:80px;top:588px;width:800px;font-size:10.4px;line-height:14.5px;text-align:justify;text-align-last:center;color:#222}
.rule-h{height:0;border-top:1px dotted var(--rule)}
.rule-v{width:0;border-left:1px dotted var(--rule)}
.section-title{font:500 17px "Raleway",sans-serif;color:var(--teal);letter-spacing:.3px}
.auction-sub{font:500 12px "Roboto",sans-serif;letter-spacing:.6px;color:#111}
.thumb{width:142px;height:87px;background:linear-gradient(180deg,#3f7fd0 0%,#8db4e2 45%,#cfd3d6 65%,#5e8f3a 100%)}
.auction-type{font:600 12px "Raleway",sans-serif;color:var(--amber);letter-spacing:.3px}
.auction-info{font-size:11.2px;font-style:italic;line-height:14.5px;color:#222}
.auction-info b{font-weight:500}
.btn-sm{height:23px;border-radius:4px;color:#fff;font:500 10.5px/23px "Roboto",sans-serif;display:flex;align-items:center;justify-content:center;gap:5px}
.btn-gallery{background:var(--teal)}
.btn-details{background:#000}
.news-thumb{width:55px;height:42px;border:1px solid #ccc;background:linear-gradient(135deg,#6a9bd6,#c9a77e 60%,#4f8cc0)}
.news-title{font-size:12px;color:var(--amber)}
.news-body{font-size:9.6px;line-height:14.5px;color:#222;text-align:justify}
.news-date{font-size:9.6px;font-style:italic;text-align:right}
.quote{left:599px;top:883px;width:269px;height:156px;background:var(--teal);border-radius:12px;color:#fff;font-size:9.6px;font-style:italic;line-height:19.2px;padding:14px 16px 0 14px;text-align:justify}
.quote .mark{font:700 16px Georgia,serif;font-style:normal;vertical-align:-4px}
.avatar{left:834px;top:1057px;width:46px;height:41px;border:2px solid #eee;background:linear-gradient(160deg,#4a8fb8,#c89868)}
.byline{left:640px;top:1066px;width:185px;text-align:right;font-size:9.6px;font-style:italic;line-height:14.5px;color:#333}
.footer{left:0;top:1107px;width:960px;height:93px;background:var(--footer)}
.footer-info{left:81px;top:1119px;color:#fff;font-size:11.4px;line-height:18.5px;letter-spacing:.2px}
.footer-logo{left:700px;top:1118px;width:180px;text-align:right;color:#fff;font-size:32px;line-height:34px}
.footer-logo small{display:block;font-size:18px;line-height:22px;letter-spacing:2px}
</style>
</head>
<body>

<header>
  <div class="abs brand site-logo">BRENMOOR<small>AUCTIONS inc.</small></div>
  <form class="abs signup">
    <div class="field" style="top:11px">Your Name</div>
    <div class="field" style="top:37px">Your Email</div>
    <div class="btn">SUBMIT</div>
  </form>
  <nav class="abs nav">
    <a class="active" href="#">HOME</a>
    <a href="#">CURRENT AUCTIONS</a>
    <a href="#">PAST AUCTIONS</a>
    <a href="#">MEET THE STAFF</a>
    <a href="#">FOR SELLERS</a>
    <a href="#">FOR BUYERS</a>
    <a href="#">TESTIMONIALS</a>
    <a href="#">CONTACT US</a>
  </nav>
</header>

<svg class="abs band" width="960" height="430" viewBox="0 0 960 430" aria-hidden="true">
  <path d="M0 0H960V374Q480 484 0 374Z" fill="#e2e2e2"/>
</svg>
<div class="abs hero" role="img" aria-label="Slideshow photo: real estate agent in a suit standing in front of a suburban house with a green lawn"></div>

<h1 class="abs welcome">WELCOME TO BRENMOOR</h1>
<p class="abs intro">Lorem ipsum dolor sit amet, consectetur adipisicing elit, sed do eiusmod tempor incididunt ut labore et dolore magna aliqua. Ut enim ad minim veniam, quis nostrud exercitation ullamco laboris nisi ut aliquip ex ea commodo consequat. Duis aute irure dolor in reprehenderit in voluptate velit esse cillum dolore eu fugiat nulla pariatur. Excepteur sint occaecat cupidatat non proident, sunt in culpa qui officia deserunt mollit anim id est laborum.is simply dummy text of the printing and typesetting industry. Lorem Ipsum has been the industry's</p>

<div class="abs rule-h" style="left:79px;top:662px;width:801px"></div>
<div class="abs rule-v" style="left:587px;top:667px;height:440px"></div>

<!-- Featured auction 1 -->
<section>
  <h2 class="abs section-title" style="left:79px;top:672px">FEATURED AUCTIONS</h2>
  <div class="abs auction-sub" style="left:80px;top:700px">SHOP EQUIPMENT/TOOLS * PORK PROCESSING ITEMS</div>
  <div class="abs thumb" style="left:79px;top:727px" role="img" aria-label="Photo of a two-storey family house"></div>
  <div class="abs auction-type" style="left:239px;top:726px">LIVE ON-SITE AUCTION</div>
  <div class="abs auction-info" style="left:239px;top:745px"><b>Begins:</b> Tuesday, April23, 2014 at 10:00 am edt</div>
  <div class="abs auction-info" style="left:239px;top:764px"><b>Location:</b> Cedar Ridge Entrance- 1870 N. Valley Hwy 14<br>Cedar Ridge Rd (Auction Property)<br>Lake Orin, FL 55318</div>
  <div class="abs btn-sm btn-gallery" style="left:371px;top:806px;width:73px">
    <svg width="14" height="12" viewBox="0 0 14 12"><rect x="1" y="1" width="12" height="10" fill="none" stroke="#fff" stroke-width="1.4"/><path d="M3 9l3-4 2 3 2-2 2 3z" fill="#fff"/></svg>Gallery</div>
  <div class="abs btn-sm btn-details" style="left:451px;top:806px;width:73px">
    <svg width="16" height="10" viewBox="0 0 16 10"><rect x="0" y="1" width="7" height="8" rx="1.5" fill="#fff"/><path d="M9 2h7M9 5h7M9 8h7" stroke="#fff" stroke-width="1.2"/></svg>Details</div>
</section>

<div class="abs rule-h" style="left:79px;top:865px;width:508px"></div>

<!-- Featured auction 2 -->
<section>
  <h2 class="abs section-title" style="left:79px;top:879px">FEATURED AUCTIONS</h2>
  <div class="abs auction-sub" style="left:80px;top:907px">SHOP EQUIPMENT/TOOLS * PORK PROCESSING ITEMS</div>
  <div class="abs thumb" style="left:79px;top:934px" role="img" aria-label="Photo of a two-storey family house"></div>
  <div class="abs auction-type" style="left:239px;top:933px">LIVE ON-SITE AUCTION</div>
  <div class="abs auction-info" style="left:239px;top:952px"><b>Begins:</b> Tuesday, April23, 2014 at 10:00 am edt</div>
  <div class="abs auction-info" style="left:239px;top:971px"><b>Location:</b> Cedar Ridge Entrance- 1870 N. Valley Hwy 14<br>Cedar Ridge Rd (Auction Property)<br>Lake Orin, FL 55318</div>
  <div class="abs btn-sm btn-gallery" style="left:371px;top:1013px;width:73px">
    <svg width="14" height="12" viewBox="0 0 14 12"><rect x="1" y="1" width="12" height="10" fill="none" stroke="#fff" stroke-width="1.4"/><path d="M3 9l3-4 2 3 2-2 2 3z" fill="#fff"/></svg>Gallery</div>
  <div class="abs btn-sm btn-details" style="left:451px;top:1013px;width:73px">
    <svg width="16" height="10" viewBox="0 0 16 10"><rect x="0" y="1" width="7" height="8" rx="1.5" fill="#fff"/><path d="M9 2h7M9 5h7M9 8h7" stroke="#fff" stroke-width="1.2"/></svg>Details</div>
</section>

<!-- News & events -->
<aside>
  <h2 class="abs section-title" style="left:621px;top:672px">NEWS &amp; EVENTS</h2>

  <div class="abs news-thumb" style="left:596px;top:712px" role="img" aria-label="Thumbnail of a house with a sold sign"></div>
  <div class="abs news-title" style="left:663px;top:709px">Lorem ipsum dolor sit amet,</div>
  <div class="abs news-body" style="left:663px;top:724px;width:216px">consectetur adipisicing elit, sed do eiusmod tempor incididunt ut labore et .</div>
  <div class="abs news-date" style="left:663px;top:756px;width:216px">January 13, 2013</div>
  <div class="abs rule-h" style="left:588px;top:784px;width:292px"></div>

  <div class="abs news-thumb" style="left:596px;top:798px" role="img" aria-label="Thumbnail of a house with a sold sign"></div>
  <div class="abs news-title" style="left:663px;top:795px">Lorem ipsum dolor sit amet,</div>
  <div class="abs news-body" style="left:663px;top:810px;width:216px">consectetur adipisicing elit, sed do eiusmod tempor incididunt ut labore et .</div>
  <div class="abs news-date" style="left:663px;top:842px;width:216px">January 13, 2013</div>
  <div class="abs rule-h" style="left:588px;top:865px;width:292px"></div>

  <blockquote class="abs quote"><span class="mark">&ldquo;</span> Lorem ipsum dolor sit amet, consectetur adipisicing elit, sed do eiusmod tempor incididunt ut labore et dolore magna aliqua. Ut enim ad minim veniam, quis nostrud exercitation ullamco laboris teur sint occaecat cupidatat non proident, sunt in culpa qui officia deserunt mollit anim id est laborum. <span class="mark">&rdquo;</span></blockquote>
  <svg class="abs" style="left:800px;top:1037px" width="26" height="28" viewBox="0 0 26 28" aria-hidden="true"><path d="M4 0H22L24 27Z" fill="#0e8284"/></svg>
  <div class="abs byline">By Dale Ferris<br>Posted on Nov12,2012</div>
  <div class="abs avatar" role="img" aria-label="Testimonial author portrait"></div>
</aside>

<footer>
  <div class="abs footer"></div>
  <div class="abs footer-info">
    Phone: (502) 736 2048<br>
    Email: office@brenmoorbid.example<br>
    Address: Brenmoor Auctions, Inc. 8415 Tamsen Rd., Louisville KY 40291
  </div>
  <div class="abs brand footer-logo">BRENMOOR<small>AUCTIONS inc.</small></div>
</footer>

</body>
</html>
```